Advertisement flyer (editable) and market report template in same style

Advertisement flyer (aka 1 page Media Kit) for us to sell advertising space on our website banner, harborlumenquay.com, and a market report template in the same style.
We would like to use colors that are used on our website. The flyer and market report template should be simple, and professional-looking. It should not look "old" or "boring". I've attached two drafts (1 each respectively), and our logo.

Target Market(s)

30-60 year old men but should look cool, new-aged, and fresh.

Industry/Entity Type

Shipping

Font styles to use
Serif

Requirements
Must have
• Editable layout so we can adjust text, numbers, and graphics on all. A fresh and new look. Colors per www.HarborLumenQuay.com website.
Should not have
• Boring layout and font

```html
<!DOCTYPE html>
<html lang="en">
<head>
<meta charset="utf-8">
<title>HLQ Weekly Search Marketing Report</title>
<link href="https://fonts.googleapis.com/css2?family=Cabin:wght@400;500;600&display=swap" rel="stylesheet">
<style>
:root{
  --navy:#284a7e;
  --navy-row:#2d5189;
  --slate:#505a68;
  --ice:#dde9f5;
  --panel:#eaecef;
  --ink:#1f2a38;
  --heading:#2c4b7e;
  --white:#ffffff;
  --up:#2fae3f;
  --down:#e0262b;
}
*{box-sizing:border-box;margin:0;padding:0}
html,body{width:1200px;height:3226px;overflow:hidden;background:var(--white)}
body{position:relative;font-family:"Cabin",sans-serif;color:var(--ink)}
.band{position:absolute;left:673px;width:527px}
.band--dark{background:var(--navy)}
.band--light{background:var(--panel)}
.brand{position:absolute;left:78px;top:70px;font-size:40px;font-weight:600;color:var(--navy);display:flex;align-items:center;gap:14px}
.brand-dot{width:22px;height:22px;border-radius:50%;background:var(--navy)}
.issue-date{position:absolute;left:78px;top:172px;font-size:38px;color:#3a6db3}
.report-title{position:absolute;left:673px;width:527px;top:128px;text-align:center;color:var(--white);font-size:40px;line-height:1.15}
.section-title{position:absolute;left:0;width:673px;text-align:center;color:var(--heading);font-size:41px;font-weight:500}
.section-title--big{font-size:58px}
.rates{position:absolute;left:47px;width:598px;border-collapse:collapse;font-size:21px}
.rates caption{background:var(--navy);color:var(--white);font-size:30px;height:47px;line-height:50px}
.rates thead th{background:var(--navy);color:var(--white);font-weight:400;height:43px;font-size:21px;line-height:1}
.rates thead th small{display:block;font-size:20px}
.rates td{height:58px;text-align:center}
.rates td.label{background:var(--slate);color:var(--white);text-align:left;padding-left:22px;width:170px}
.rates--wide td.label{width:245px}
.rates tr.light td:not(.label){background:var(--ice)}
.rates tr.dark td:not(.label){background:var(--navy-row);color:var(--white)}
.chg{display:inline-flex;align-items:center;gap:18px}
.chg svg{width:16px;height:24px}
.notes{position:absolute;left:720px;width:430px;font-size:22px;line-height:1.08;text-align:justify;color:var(--ink)}
.notes p+p{margin-top:10px}
.chart{position:absolute;left:47px;top:1505px}
.handy-area{position:absolute;left:0;top:2413px;width:1200px;height:340px;background:var(--panel)}
.handy-box{position:absolute;left:44px;top:34px;width:1112px;height:258px;background:#f6f7f9;border:2px solid #d4d8dd;border-radius:14px}
</style>
</head>
<body>

<div class="band band--dark" style="top:0;height:237px"></div>
<div class="band band--light" style="top:237px;height:365px"></div>
<div class="band band--dark" style="top:602px;height:118px"></div>
<div class="band band--light" style="top:720px;height:259px"></div>
<div class="band band--dark" style="top:979px;height:118px"></div>
<div class="band band--light" style="top:1097px;height:742px"></div>
<div class="band band--dark" style="top:1839px;height:107px"></div>
<div class="band band--light" style="top:1946px;height:377px"></div>
<div class="band band--dark" style="top:2323px;height:90px"></div>
<div class="band band--dark" style="top:2753px;height:118px"></div>
<div class="band band--light" style="top:2871px;height:269px"></div>
<div class="band band--dark" style="top:3140px;height:86px"></div>

<header>
  <div class="brand"><span class="brand-dot"></span>HarborLumenQuay</div>
  <div class="issue-date">September 28, 2016</div>
  <h1 class="report-title" style="font-weight:400">HLQ Weekly<br>Search Marketing Report</h1>
</header>

<h2 class="section-title" style="top:266px">Crude Prices</h2>
<table class="rates" style="top:340px">
  <caption>Crude Prices</caption>
  <thead><tr><th style="text-align:left;padding-left:22px">$/bbl</th><th>22- Sep</th><th>15-Sep</th><th><small>W-O-W</small>Change</th></tr></thead>
  <tbody>
    <tr class="light"><td class="label">ICE Brent</td><td>47.29</td><td>46.30</td><td><span class="chg">0.99<svg viewBox="0 0 16 24"><path d="M8 1 15 10H10V23H6V10H1Z" fill="var(--up)"/></svg></span></td></tr>
    <tr class="dark"><td class="label">Dtd Brent</td><td>47.29</td><td>46.30</td><td><span class="chg">0.99<svg viewBox="0 0 16 24"><path d="M8 1 15 10H10V23H6V10H1Z" fill="var(--up)"/></svg></span></td></tr>
    <tr class="light"><td class="label" style="text-align:center;padding:0">Dubai</td><td>44.71</td><td>42.86</td><td><span class="chg">1.85<svg viewBox="0 0 16 24"><path d="M8 1 15 10H10V23H6V10H1Z" fill="var(--up)"/></svg></span></td></tr>
  </tbody>
</table>
<div class="notes" style="top:355px">
  <p>Assignments ask for a ‘report’, rather than an essay, and students are often confused about what that really means.</p>
  <p>Likewise, in business, confronted with a request for a ‘report’ to a senior manager, many people struggle to know what to write.</p>
  <p>Confusion often arises about the writing style, what to include, the factors.</p>
</div>

<h2 class="section-title" style="top:645px">Products</h2>
<table class="rates" style="top:722px">
  <caption>Products</caption>
  <thead><tr><th style="text-align:left;padding-left:22px">$/bbl</th><th>22- Sep</th><th>15-Sep</th><th><small>W-O-W</small>Change</th></tr></thead>
  <tbody>
    <tr class="light"><td class="label">ICE Brent</td><td>47.29</td><td>46.30</td><td><span class="chg">0.99<svg viewBox="0 0 16 24"><path d="M8 1 15 10H10V23H6V10H1Z" fill="var(--up)"/></svg></span></td></tr>
    <tr class="dark"><td class="label">Dtd Brent</td><td>47.29</td><td>46.30</td><td><span class="chg">0.99<svg viewBox="0 0 16 24"><path d="M8 1 15 10H10V23H6V10H1Z" fill="var(--up)"/></svg></span></td></tr>
    <tr class="light"><td class="label" style="text-align:center;padding:0">Dubai</td><td>44.71</td><td>42.86</td><td><span class="chg">1.85<svg viewBox="0 0 16 24"><path d="M8 1 15 10H10V23H6V10H1Z" fill="var(--up)"/></svg></span></td></tr>
  </tbody>
</table>
<div class="notes" style="top:731px">
  <p>Assignments ask for a ‘report’, rather than an essay, and students are often confused about what that really means.</p>
  <p>Likewise, in business, confronted with a request for a ‘report’ to a senior manager, many people struggle to know what to write.</p>
  <p>Confusion often arises about the writing style, what to include, the factors.</p>
</div>

<h2 class="section-title" style="top:1024px">VLCC</h2>
<table class="rates" style="top:1101px">
  <caption>Spot VLCC Rates</caption>
  <thead><tr><th style="text-align:left;padding-left:22px">$/bbl</th><th>22- Sep</th><th>15-Sep</th><th><small>W-O-W</small>Change</th></tr></thead>
  <tbody>
    <tr class="light"><td class="label">AG/USGC</td><td>25.00</td><td>22.00</td><td><span class="chg">3.00<svg viewBox="0 0 16 24"><path d="M8 1 15 10H10V23H6V10H1Z" fill="var(--up)"/></svg></span></td></tr>
    <tr class="dark"><td class="label">AG/Japan</td><td>38.00</td><td>32.00</td><td><span class="chg">6.00<svg viewBox="0 0 16 24"><path d="M8 1 15 10H10V23H6V10H1Z" fill="var(--up)"/></svg></span></td></tr>
    <tr class="light"><td class="label">AG/Singapore</td><td>39.00</td><td>33.00</td><td><span class="chg">6.00<svg viewBox="0 0 16 24"><path d="M8 1 15 10H10V23H6V10H1Z" fill="var(--up)"/></svg></span></td></tr>
    <tr class="dark"><td class="label">WAF/USGC</td><td>42.50</td><td>45.00</td><td><span class="chg">-2.50<svg viewBox="0 0 16 24"><path d="M8 23 15 14H10V1H6V14H1Z" fill="var(--down)"/></svg></span></td></tr>
    <tr class="light"><td class="label">WAF/Far East</td><td>48.50</td><td>42.50</td><td><span class="chg">6.00<svg viewBox="0 0 16 24"><path d="M8 1 15 10H10V23H6V10H1Z" fill="var(--up)"/></svg></span></td></tr>
  </tbody>
</table>
<div class="notes" style="top:1108px">
  <p>Assignments ask for a ‘report’, rather than an essay, and students are often confused about what that really means.</p>
  <p>Likewise, in business, confronted with a request for a ‘report’ to a senior manager, many people struggle to know what to write.</p>
  <p>Confusion often arises about the writing style, what to include, the factors.</p>
</div>
<div class="notes" style="top:1409px">
  <p>Assignments ask for a ‘report’, rather than an essay, and students are often confused about what that really means.</p>
  <p>Likewise, in business, confronted with a request for a ‘report’ to a senior manager, many people struggle to know what to write.</p>
  <p>Confusion often arises about the writing style, what to include, the factors.</p>
</div>

<svg class="chart" width="420" height="330" viewBox="0 0 420 330" font-family="Cabin, sans-serif" font-size="15" fill="#333">
  <g text-anchor="end">
    <text x="20" y="14">4.5</text><text x="20" y="50">4.0</text><text x="20" y="86">3.5</text>
    <text x="20" y="122">3.0</text><text x="20" y="158">2.5</text><text x="20" y="194">2.0</text>
    <text x="20" y="230">1.5</text><text x="20" y="266">1.0</text><text x="20" y="302">0.5</text>
    <text x="20" y="320">0.0</text>
  </g>
  <line x1="30" y1="315" x2="410" y2="315" stroke="#999"/>
  <polyline fill="none" stroke="#1f5372" stroke-width="5" stroke-linejoin="round"
    points="38,250 42,270 48,262 55,268 62,240 68,252 74,225 80,255 86,220 92,248 98,210 104,238 110,200 116,226 120,190 126,150 132,180 138,135 144,160 150,120 156,160 162,105 168,140 172,100 176,90 180,105 184,88 188,120 192,175 198,210 204,190 210,220 216,200 222,210 228,240 234,226 240,250 246,222 252,245 258,256 264,230 270,240 276,275 282,250 288,262 294,215 300,195 306,230 312,235 318,255 324,245 330,275 336,270 342,282 348,265 354,292 360,285 366,292 372,290 378,300 384,290 388,300 392,280 396,292 400,268"/>
  <g text-anchor="end" font-size="15">
    <text transform="translate(48,335) rotate(-45)">Jan-15</text>
    <text transform="translate(108,335) rotate(-45)">Apr-15</text>
    <text transform="translate(168,335) rotate(-45)">Jul-15</text>
    <text transform="translate(228,335) rotate(-45)">Oct-15</text>
    <text transform="translate(288,335) rotate(-45)">Jan-16</text>
    <text transform="translate(348,335) rotate(-45)">Apr-16</text>
    <text transform="translate(408,335) rotate(-45)">Jul-16</text>
  </g>
</svg>

<h2 class="section-title" style="top:1888px">MR/LR</h2>
<table class="rates rates--wide" style="top:1951px">
  <caption>Spot MR/LR Rates</caption>
  <thead><tr><th style="text-align:left;padding-left:22px">WS</th><th>22- Sep</th><th>15-Sep</th><th><small>W-O-W</small>Change</th></tr></thead>
  <tbody>
    <tr class="light"><td class="label">AG/Japan (75 kt)</td><td>55.00</td><td>67.50</td><td><span class="chg">3.00<svg viewBox="0 0 16 24"><path d="M8 23 15 14H10V1H6V14H1Z" fill="var(--down)"/></svg></span></td></tr>
    <tr class="light"><td class="label">AG/Japan (55 kt)</td><td>80.00</td><td>82.50</td><td><span class="chg">6.00<svg viewBox="0 0 16 24"><path d="M8 23 15 14H10V1H6V14H1Z" fill="var(--down)"/></svg></span></td></tr>
    <tr class="light"><td class="label">AG/Japan (30 kt)</td><td>100.00</td><td>92.50</td><td><span class="chg">6.00<svg viewBox="0 0 16 24"><path d="M8 1 15 10H10V23H6V10H1Z" fill="var(--up)"/></svg></span></td></tr>
    <tr class="dark"><td class="label">Singapore/Japan (30 kt)</td><td>117.00</td><td>117.50</td><td><span class="chg">-2.50<svg viewBox="0 0 16 24"><path d="M8 23 15 14H10V1H6V14H1Z" fill="var(--down)"/></svg></span></td></tr>
  </tbody>
</table>
<div class="notes" style="top:1964px">
  <p>Assignments ask for a ‘report’, rather than an essay, and students are often confused about what that really means.</p>
  <p>Likewise, in business, confronted with a request for a ‘report’ to a senior manager, many people struggle to know what to write.</p>
  <p>Confusion often arises about the writing style, what to include, the factors.</p>
</div>

<h2 class="section-title section-title--big" style="top:2328px">Handy</h2>
<div class="handy-area"><div class="handy-box"></div></div>

<h2 class="section-title section-title--big" style="top:2788px">Bunker</h2>
<table class="rates rates--wide" style="top:2882px;font-size:20px">
  <caption>Bunker Prices</caption>
  <thead><tr><th style="text-align:left;padding-left:22px">$/T</th><th>22- Sep</th><th>15-Sep</th><th><small>W-O-W</small>Change</th></tr></thead>
  <tbody>
    <tr class="light"><td class="label">Singapore 380 cst</td><td>255.00</td><td>258.00</td><td><span class="chg">-3.00<svg viewBox="0 0 16 24"><path d="M8 23 15 14H10V1H6V14H1Z" fill="var(--down)"/></svg></span></td></tr>
    <tr class="light"><td class="label">Singapore 180 cst</td><td>266.00</td><td>271.00</td><td><span class="chg">-5.00<svg viewBox="0 0 16 24"><path d="M8 23 15 14H10V1H6V14H1Z" fill="var(--down)"/></svg></span></td></tr>
    <tr class="light"><td class="label">Gasoil</td><td>412.00</td><td>415.00</td><td><span class="chg">-3.00<svg viewBox="0 0 16 24"><path d="M8 23 15 14H10V1H6V14H1Z" fill="var(--down)"/></svg></span></td></tr>
  </tbody>
</table>

</body>
</html>
```